Brisk Harbor Funding - Letterhead

We need letterhead options for our case funding company called Brisk Harbor Funding. Here are some of the details:

Name - Brisk Harbor Funding
Phone - (555) 214 - 9083
Address - 38 Larkmoor Avenue
Suite 412
New York, NY 10958
Website - briskharborfunding.example

```html
<!DOCTYPE html>
<html lang="en">
<head>
<meta charset="utf-8">
<title>Brisk Harbor Funding – Letterhead</title>
<link rel="stylesheet" href="https://fonts.googleapis.com/css2?family=Source+Sans+3:wght@400;600&family=Arimo:wght@700&display=swap">
<style>
  :root {
    --navy: #06334f;
    --steel: #8e9aa4;
    --paper: #f5f5f5;
    --backdrop: #e4e4e4;
    --ink: #4a4a4a;
    --ink-strong: #3f3f3f;
    --sig-tone: #d9d9d9;
  }
  * { box-sizing: border-box; margin: 0; padding: 0; }
  html, body { width: 1134px; height: 1200px; overflow: hidden; }
  body {
    background: var(--backdrop);
    font-family: "Source Sans 3", "Myriad Pro", sans-serif;
    position: relative;
  }
  .letterhead {
    position: absolute;
    left: 156px; top: 20px;
    width: 822px; height: 1160px;
    background: var(--paper);
    overflow: hidden;
  }
  .side-bands { position: absolute; left: 0; top: 0; width: 60px; height: 1160px; }
  .site-url {
    position: absolute;
    left: 20px; top: 1133px;
    transform: rotate(-90deg);
    transform-origin: 0 0;
    color: #ffffff;
    font-size: 12px;
    white-space: nowrap;
    translate: -7px 0;
  }
  .brand {
    position: absolute;
    left: 77px; top: 58px;
    display: flex; align-items: center; gap: 12px;
  }
  .brand-mark { width: 46px; height: 46px; background: var(--navy); }
  .brand-name {
    color: var(--navy);
    font-weight: 600;
    font-size: 17px;
    line-height: 18px;
    letter-spacing: 1.6px;
    text-transform: uppercase;
  }
  .contact {
    position: absolute;
    left: 557px; top: 66px;
    font-size: 11.5px;
    line-height: 16px;
    color: #1f2f3d;
  }
  .contact-row { display: flex; align-items: center; gap: 4px; }
  .contact-row svg { flex: none; }
  .contact-row.phone { color: var(--navy); }
  .contact-address { display: flex; gap: 8px; margin-top: 10px; }
  .greeting {
    position: absolute;
    left: 83px; top: 264px;
    font-family: "Arimo", Arial, sans-serif;
    font-weight: 700;
    font-size: 17.5px;
    color: var(--ink-strong);
  }
  .letter-body {
    position: absolute;
    left: 84px; top: 312px;
    width: 655px;
    font-size: 16.4px;
    line-height: 21.4px;
    color: var(--ink);
  }
  .letter-body p { text-align: justify; margin-bottom: 21.4px; }
  .signature {
    position: absolute;
    left: 84px; top: 831px;
    width: 154px; height: 75px;
    background: linear-gradient(90deg, var(--sig-tone), #ececec);
    border-radius: 4px;
  }
</style>
</head>
<body>
  <main class="letterhead">
    <svg class="side-bands" viewBox="0 0 60 1160" aria-hidden="true">
      <path d="M0 0 H14 C18 400 28 800 39 1160 H0 Z" fill="var(--navy)"/>
      <path d="M24 0 H41 C40 330 40.5 660 41 975 C34 650 29 320 24 0 Z" fill="var(--steel)"/>
    </svg>
    <span class="site-url">www.briskharborfunding.example</span>

    <div class="brand">
      <span class="brand-mark"></span>
      <div class="brand-name">Brisk<br>Harbor<br>Funding</div>
    </div>

    <address class="contact" style="font-style:normal">
      <div class="contact-row phone">
        <svg width="9" height="9" viewBox="0 0 10 10"><path d="M2 1 L4 1 L4.6 3 L3.4 4 Q4.5 6 6 6.6 L7 5.4 L9 6 L9 8 Q5 9 1.5 5 Q1 3 2 1 Z" fill="var(--navy)"/></svg>
        (555) 214 - 9083
      </div>
      <div class="contact-row">
        <svg width="9" height="7" viewBox="0 0 10 7"><rect width="10" height="7" fill="var(--navy)"/><path d="M0 0 L5 4 L10 0" stroke="#fff" fill="none" stroke-width="1"/></svg>
        sales@briskharborfunding.example
      </div>
      <div class="contact-address">
        <svg width="9" height="13" viewBox="0 0 10 14"><path d="M5 0 A5 5 0 0 1 10 5 C10 8 5 14 5 14 C5 14 0 8 0 5 A5 5 0 0 1 5 0 Z" fill="var(--navy)"/><circle cx="5" cy="5" r="2" fill="var(--paper)"/></svg>
        <div>38 Larkmoor Avenue Suite 412<br>New York, NY 10958</div>
      </div>
    </address>

    <h1 class="greeting">Dear Mr. John,</h1>

    <section class="letter-body">
      <p>Lorem Ipsum is simply dummy text of the printing and typesetting industry. Lorem Ipsum has been the industry's standard dummy text ever since the 1500s, when an unknown printer took a galley of type and scrambled it to make a type specimen book. It has survived not only five centuries, but also the leap into electronic typesetting, remaining essentially unchanged.</p>
      <p>The standard chunk of Lorem Ipsum used since the 1500s is reproduced below for those interested. Sections 1.10.32 and 1.10.33 from "de Finibus Bonorum et Malorum" by Marcus Vell are also reproduced in their exact original form, accompanied by English versions from the 1914 translation by H. Dunmore</p>
      <p>Lorem Ipsum is simply dummy text of the printing and typesetting industry. Lorem Ipsum has been the industry's standard dummy text ever since the 1500s, when an unknown printer took a galley of type and scrambled it to make a type specimen book. It has survived not only five centuries, but also the leap into electronic typesetting, remaining essentially unchanged. It was popularised in the</p>
      <p>Lorem Ipsum is simply dummy text of the printing and typesetting industry. Lorem Ipsum has been the industry's standard dummy text ever since the 1500s, when an unknown printer took a galley of type and scrambled it to make a type specimen book. It has survived not only five centuries, but also the leap into electronic typesetting, remaining essentially unchanged. It was popularised in the</p>
    </section>

    <div class="signature" role="img" aria-label="Handwritten signature of the sender"></div>
  </main>
</body>
</html>
```